Road Construction Company needs business cards

We would like a new business card designed for our business.

We're a road construction company based in Qld, Australia.

Can the business card please have the following information on it.

Name: Brent Malvoy
Position: General Manager
Phone: 0471 592 304
Email: Brent.malvoy@quendix.com.au
Address: 87 Harrowgate Ave, Pindarra, QLD, 4000
Website: www.quendix.com.au

Visually we'd like the card to be professional and simple.

Attached is our logo.

Our website is www.quendix.com.au

Target Market(s)

Men aged 25-60

Contact Information for Business Card

As listed in project description

Font styles to use
Serif

Requirements
Must have
• Large logo on back of card

```html
<!DOCTYPE html>
<html lang="en">
<head>
<meta charset="utf-8">
<title>Quendix Business Card</title>
<link href="https://fonts.googleapis.com/css2?family=Montserrat:wght@400;500;800&display=swap" rel="stylesheet">
<style>
  :root {
    --backdrop: #3b3b3d;
    --card-white: #ffffff;
    --card-black: #1e1e20;
    --brand-blue: #3aa2dc;
    --brand-navy: #1a5fae;
    --ink: #2b2b2b;
    --paper-white: #ffffff;
  }
  * { margin: 0; padding: 0; box-sizing: border-box; }
  html, body { width: 1200px; height: 1200px; overflow: hidden; }
  body {
    background: var(--backdrop);
    font-family: "Montserrat", Arial, sans-serif;
    display: flex;
    flex-direction: column;
    align-items: center;
    justify-content: center;
    gap: 60px;
  }
  .card {
    position: relative;
    width: 800px;
    height: 490px;
    border-radius: 34px;
    border-bottom: 4px solid var(--brand-blue);
    overflow: hidden;
  }
  .card--front { background: var(--card-white); }
  .card--back {
    background: var(--card-black);
    display: flex;
    align-items: center;
    justify-content: center;
  }
  .wordmark {
    font-weight: 800;
    letter-spacing: 2px;
    line-height: 1;
    white-space: nowrap;
  }
  .card--front .wordmark {
    position: absolute;
    top: 150px;
    right: 70px;
    font-size: 56px;
    color: var(--brand-navy);
  }
  .card--back .wordmark {
    font-size: 112px;
    color: var(--paper-white);
  }
  .contact {
    position: absolute;
    left: 70px;
    top: 250px;
    color: var(--ink);
  }
  .contact__name {
    font-size: 34px;
    font-weight: 500;
    color: var(--brand-blue);
    text-transform: uppercase;
    line-height: 1;
  }
  .contact__role {
    font-size: 19px;
    text-transform: uppercase;
    margin-bottom: 16px;
  }
  .contact__list { list-style: none; }
  .contact__item {
    display: flex;
    align-items: flex-start;
    gap: 12px;
    font-size: 20px;
    line-height: 1.3;
    margin-bottom: 2px;
  }
  .contact__item:first-child { font-size: 24px; }
  .contact__icon {
    width: 24px;
    height: 24px;
    flex: none;
    margin-top: 2px;
    fill: var(--brand-blue);
  }
</style>
</head>
<body>
  <section class="card card--front">
    <div class="wordmark">QUENDIX</div>
    <div class="contact">
      <h1 class="contact__name">Brent Malvoy</h1>
      <p class="contact__role">General Manager</p>
      <ul class="contact__list">
        <li class="contact__item">
          <svg class="contact__icon" viewBox="0 0 24 24"><path d="M6.6 10.8a15.1 15.1 0 0 0 6.6 6.6l2.2-2.2a1 1 0 0 1 1-.25 11.4 11.4 0 0 0 3.6.57 1 1 0 0 1 1 1V20a1 1 0 0 1-1 1A17 17 0 0 1 3 4a1 1 0 0 1 1-1h3.5a1 1 0 0 1 1 1c0 1.25.2 2.45.57 3.57a1 1 0 0 1-.25 1z"/></svg>
          <span>0471 592 304</span>
        </li>
        <li class="contact__item">
          <svg class="contact__icon" viewBox="0 0 24 24"><path d="M2 5h20v14H2z M2 5l10 8 10-8" fill="none" stroke="#3aa2dc" stroke-width="2"/></svg>
          <span>Brent.malvoy@quendix.com.au</span>
        </li>
        <li class="contact__item">
          <svg class="contact__icon" viewBox="0 0 24 24"><g fill="none" stroke="#3aa2dc" stroke-width="1.8"><circle cx="12" cy="12" r="10"/><ellipse cx="12" cy="12" rx="4.5" ry="10"/><path d="M2 12h20M4 7h16M4 17h16"/></g></svg>
          <span>www.quendix.com.au</span>
        </li>
        <li class="contact__item">
          <svg class="contact__icon" viewBox="0 0 24 24"><path d="M12 2a7 7 0 0 0-7 7c0 5.2 7 13 7 13s7-7.8 7-13a7 7 0 0 0-7-7zm0 9.5A2.5 2.5 0 1 1 12 6.5a2.5 2.5 0 0 1 0 5z"/></svg>
          <span>87 Harrowgate Ave<br>Pindarra, QLD, 4000</span>
        </li>
      </ul>
    </div>
  </section>

  <section class="card card--back">
    <div class="wordmark">QUENDIX</div>
  </section>
</body>
</html>
```